High-end construction company needs a business card design

We need a modern looking business card that draws people in, is memorable and looks so good people will want to sick it on their fridges.
On the first side what is needed are:
Logo
My name - Tomas Brevik
Title - Managing Director
Website - www.kelvora.co.uk
Email - tomas@kelvora.co.uk
Telephone - 020 4917 2365
Mobile - 07845139072
On the back side was is needed is a list of all the services we provide:
-Kitchen Renovations
-Bathroom Renovations
-House Renovations
-Garage Conversions
-Extensions
-Loft Conversions
-Conservatories
-Carpentry
-Tiling
-Electrical
-Plumbing & Heating
-Bricklaying
-Landscaping
-Decorating
-Plastering
We would like the colours to be the same shades as on the logo with grey or black for the words.
Target Market(s)
Anyone who needs building work done
Contact Information for Business Card
This business card is for a construction company which strives to deliver excellent service and quality.
The look and feel of the card should represent this.
Requirements
Must have
- On the first side what is needed are:
Logo
My name - Tomas Brevik
Title - Managing Director
Website - www.kelvora.co.uk
Email - tomas@kelvora.co.uk
Telephone - 020 4917 2365
Mobile - 07845139072
Nice to have
- Cool looking features

```html
<!DOCTYPE html>
<html lang="en">
<head>
<meta charset="utf-8">
<title>Kelvora Construction – Business Card</title>
<link rel="stylesheet" href="https://fonts.googleapis.com/css2?family=Open+Sans:wght@400;600;700;800&display=swap">
<style>
  :root {
    --green-dark: #4a8a3c;
    --green-light: #72b843;
    --green-pale: #9fd06f;
    --card-white: #f4f4f4;
    --ink: #2b2b2b;
    --backdrop: #e4e4e4;
  }
  * { margin: 0; padding: 0; box-sizing: border-box; }
  html, body { width: 1200px; height: 960px; overflow: hidden; }
  body {
    background: var(--backdrop);
    font-family: "Open Sans", Arial, sans-serif;
    position: relative;
  }
  .card {
    position: absolute;
    left: 330px;
    width: 543px;
    height: 351px;
    overflow: hidden;
  }
  .card-back { top: 112px; background: var(--green-dark); }
  .card-front { top: 505px; background: var(--card-white); }

  /* Back side */
  .back-shapes { position: absolute; inset: 0; }
  .hero-art {
    position: absolute;
    left: 0; top: 40px;
    width: 335px; height: 250px;
    background: linear-gradient(135deg, #5c9c45 0%, #6aae43 60%, #4f8e3e 100%);
    clip-path: polygon(0 60%, 60% 0, 100% 20%, 100% 100%, 0 100%);
  }
  .services {
    position: absolute;
    right: 28px; top: 32px;
    list-style: none;
    text-align: right;
    color: #ffffff;
    font-size: 14.5px;
    line-height: 19.2px;
    letter-spacing: -0.1px;
  }
  .services li::after {
    content: "";
    display: inline-block;
    width: 5px; height: 5px;
    border-radius: 50%;
    background: var(--green-dark);
    margin-left: 6px;
    vertical-align: middle;
  }
  .back-web {
    position: absolute;
    left: 46px; top: 295px;
    color: #ffffff;
    font-size: 14px;
    letter-spacing: 1.2px;
  }

  /* Front side */
  .brand {
    position: absolute;
    left: 45px; top: 98px;
    color: var(--green-light);
    font-weight: 800;
  }
  .brand-name { display: block; font-size: 44px; line-height: 40px; letter-spacing: 1px; }
  .brand-sub { display: block; font-size: 12.5px; letter-spacing: 1.6px; margin-top: 4px; }
  .person {
    position: absolute;
    right: 41px; top: 82px;
    text-align: right;
  }
  .person-name { color: var(--green-dark); font-weight: 700; font-size: 17px; line-height: 22px; }
  .person-title { color: var(--ink); font-size: 14px; line-height: 20px; }
  .tab {
    position: absolute;
    right: 0; top: 78px;
    width: 13px; height: 47px;
    background: var(--green-light);
  }
  .contacts {
    position: absolute;
    left: 46px; top: 228px;
    list-style: none;
    color: var(--ink);
    font-size: 14px;
    line-height: 19px;
  }
  .contacts li { display: flex; align-items: center; gap: 6px; }
  .contacts svg { width: 12px; height: 12px; flex: none; }
  .faint-art {
    position: absolute;
    left: 240px; top: 155px;
    width: 303px; height: 182px;
    background: linear-gradient(90deg, rgba(114,184,67,0) 0%, rgba(114,184,67,0.12) 45%, rgba(114,184,67,0.16) 100%);
  }
  .front-band { position: absolute; left: 0; bottom: 0; width: 543px; height: 15px; }
</style>
</head>
<body>

<section class="card card-back" aria-label="Card back: services">
  <svg class="back-shapes" viewBox="0 0 543 351" width="543" height="351" aria-hidden="true">
    <polygon points="265,0 543,0 543,351 263,351 332,178" fill="var(--green-light)"/>
    <polygon points="0,290 238,290 258,320 0,320" fill="var(--green-light)"/>
  </svg>
  <div class="hero-art" role="img" aria-label="Illustration of an excavator arm above a house and city buildings"></div>
  <ul class="services">
    <li>KITCHEN RENOVATIONS</li>
    <li>BATHROOM RENOVATIONS</li>
    <li>HOUSE RENOVATIONS</li>
    <li>GARAGE CONVERSIONS</li>
    <li>EXTENSIONS</li>
    <li>LOFT CONVERSIONS</li>
    <li>CONSERVATORIES</li>
    <li>CARPENTRY</li>
    <li>ELECTRICAL</li>
    <li>PLUMBING &amp; HEATING</li>
    <li>BRICKLAYING</li>
    <li>LANDSCAPING</li>
    <li>DECORATING</li>
    <li>PLASTERING</li>
    <li>TILING</li>
  </ul>
  <p class="back-web">www.kelvora.co.uk</p>
</section>

<section class="card card-front" aria-label="Card front: contact details">
  <div class="faint-art" role="img" aria-label="Faint decorative area in pale green"></div>
  <div class="brand">
    <span class="brand-name">KELVORA</span>
    <span class="brand-sub">CONSTRUCTION LTD</span>
  </div>
  <div class="person">
    <p class="person-name">TOMAS BREVIK</p>
    <p class="person-title">Managing Director</p>
  </div>
  <div class="tab"></div>
  <ul class="contacts">
    <li>
      <svg viewBox="0 0 12 12" aria-hidden="true"><path d="M2.5 0.8l2 2.2-1 1.3c.6 1.5 1.8 2.8 3.3 3.4l1.3-1 2.2 2-1.2 1.9C5 10.3 1.5 6.8 0.8 2z" fill="var(--green-dark)"/></svg>
      020 4917 2365
    </li>
    <li>
      <svg viewBox="0 0 12 12" aria-hidden="true"><rect x="3" y="0.5" width="6" height="11" rx="1" fill="none" stroke="var(--green-dark)" stroke-width="1.3"/><rect x="5" y="9" width="2" height="1" fill="var(--green-dark)"/></svg>
      07845139072
    </li>
    <li>
      <svg viewBox="0 0 12 12" aria-hidden="true"><rect x="0.7" y="2" width="10.6" height="8" fill="none" stroke="var(--green-dark)" stroke-width="1.3"/><path d="M0.7 2.5L6 6.5l5.3-4" fill="none" stroke="var(--green-dark)" stroke-width="1.2"/></svg>
      tomas@kelvora.co.uk
    </li>
    <li>
      <svg viewBox="0 0 12 12" aria-hidden="true"><circle cx="6" cy="6" r="5.2" fill="none" stroke="var(--green-dark)" stroke-width="1.1"/><ellipse cx="6" cy="6" rx="2.2" ry="5.2" fill="none" stroke="var(--green-dark)" stroke-width="1"/><path d="M0.8 6h10.4M1.6 3.4h8.8M1.6 8.6h8.8" stroke="var(--green-dark)" stroke-width="0.9"/></svg>
      www.kelvora.co.uk
    </li>
  </ul>
  <svg class="front-band" viewBox="0 0 543 15" width="543" height="15" aria-hidden="true">
    <polygon points="0,0 365,0 350,15 0,15" fill="var(--green-dark)"/>
    <polygon points="368,0 543,0 543,15 353,15" fill="var(--green-light)"/>
  </svg>
</section>

</body>
</html>
```